A4 Client Referral Program Flyer for Property Management Agency

Harbourline Lettings Group is a property management specialist based on Sydney's Northern Beaches in Australia.

We manage mid to high-end rental properties for investors and property owners.
We are currently looking to build our portfolio and are offering existing clients and contacts a referral incentive. We want to sign up more properties to manage.

We are offering the referrer a $250 referral fee and the new owner 2 months of free management to entice them to use Harbourline Lettings Group.

We want an A4 Flyer to print and add to other document packages we hand out to clients and suppliers.
If at all possible a matching digital banner would be great too! 1000px wide x 250px

Please find copy attached in Word Doc and our logo attached also.

Please see our website for any more details on our business.

We must be able to have an editable photoshop version (PSD) of the document as well as a print ready PDF version incl any bleed necessary for A4 printing.

Target Market(s)

30-60YO Male and Female

Industry/Entity Type

Real Estate

Font styles to use
Sans Serif

Requirements
Must have
• Company Logo, contact details and copy provided

```html
<!DOCTYPE html>
<html lang="en">
<head>
<meta charset="utf-8">
<title>Harbourline Lettings Group – Referral Banners</title>
<link rel="stylesheet" href="https://fonts.googleapis.com/css2?family=Montserrat:wght@600;700&family=Arimo:wght@400;700&display=swap">
<style>
  :root {
    --stage: #a4a4a4;
    --paper: #ffffff;
    --ink: #1b1b1b;
    --teal: #2a7d8b;
    --teal-light: #3ea6b4;
    --muted: #333333;
  }
  * { box-sizing: border-box; margin: 0; padding: 0; }
  html, body { width: 1200px; height: 1200px; overflow: hidden; }
  body { background: var(--stage); position: relative; font-family: "Arimo", Arial, sans-serif; color: var(--ink); }

  .banner { position: absolute; background: var(--paper); overflow: hidden; box-shadow: 0 14px 22px rgba(0,0,0,.35); }
  .banner--arrow { left: 40px; top: 76px; width: 1114px; height: 278px; }
  .banner--slant { left: 44px; top: 462px; width: 1110px; height: 276px; }
  .banner--mosaic { left: 42px; top: 836px; width: 1112px; height: 278px; border: 2px solid var(--teal); }

  .art { position: absolute; left: 0; top: 0; }
  .abs { position: absolute; }

  .brand { font-family: "Montserrat", sans-serif; font-weight: 600; color: var(--ink); letter-spacing: -.2px; white-space: nowrap; display: flex; align-items: center; gap: 7px; }
  .brand__mark { width: 9px; height: 9px; background: var(--teal); flex: none; }

  .headline { font-family: "Montserrat", sans-serif; font-weight: 700; color: var(--ink); white-space: nowrap; }
  .offer { font-family: "Montserrat", sans-serif; font-weight: 700; color: var(--ink); white-space: nowrap; display: flex; align-items: center; gap: 6px; }
  .offer__amount { background: var(--teal); color: #fff; border-radius: 5px; padding: 1px 5px; }

  .contact { display: flex; align-items: center; gap: 8px; white-space: nowrap; color: var(--ink); }
  .contact svg { fill: var(--teal); flex: none; }
  .phone-number { font-family: "Montserrat", sans-serif; font-weight: 700; color: var(--teal); }

  .contact-row { display: flex; align-items: center; }
  .contact-row > .contact + .contact { border-left: 1px solid var(--teal); margin-left: 8px; padding-left: 8px; height: 22px; }

  .fine { display: flex; gap: 6px; align-items: flex-start; }
  .fine__label { font-weight: 700; font-size: 9px; color: var(--ink); white-space: nowrap; }
  .fine__text { font-size: 6.6px; line-height: 1.35; color: var(--muted); border-left: 1px solid var(--teal); padding-left: 4px; }

  .divider { position: absolute; background: var(--teal); }
</style>
</head>
<body>

<!-- Banner with chevron -->
<section class="banner banner--arrow">
  <svg class="art" width="1114" height="278" viewBox="0 0 1114 278">
    <defs>
      <linearGradient id="streetA" x1="0" y1="0" x2="0" y2="1">
        <stop offset="0" stop-color="#3f93d6"/>
        <stop offset=".45" stop-color="#b9c3c6"/>
        <stop offset=".7" stop-color="#4f7a3a"/>
        <stop offset="1" stop-color="#a9a59c"/>
      </linearGradient>
    </defs>
    <polygon role="img" aria-label="Photo of modern terraced homes on a leafy hillside street" points="0,0 530,0 566,139 530,278 0,278" fill="url(#streetA)"/>
    <polygon points="530,0 550,0 586,139 550,278 530,278 566,139" fill="var(--teal)"/>
    <polygon points="550,0 557,0 593,139 557,278 550,278 586,139" fill="var(--teal-light)"/>
  </svg>
  <div class="abs brand" style="right:40px; top:44px; font-size:16px;"><span class="brand__mark"></span>HARBOURLINE LETTINGS GROUP</div>
  <div class="abs headline" style="left:614px; top:110px; font-size:27px;">Invite your friends and receive</div>
  <div class="abs offer" style="left:614px; top:150px; font-size:17px;"><span class="offer__amount">$250</span>and they get 2 months free management! *</div>
  <div class="abs contact-row" style="left:618px; top:206px;">
    <div class="contact">
      <svg width="12" height="12" viewBox="0 0 24 24"><path d="M6.6 10.8a15 15 0 0 0 6.6 6.6l2.2-2.2c.3-.3.7-.4 1-.2 1.1.4 2.3.6 3.6.6.6 0 1 .4 1 1V20c0 .6-.4 1-1 1A17 17 0 0 1 3 4c0-.6.4-1 1-1h3.5c.6 0 1 .4 1 1 0 1.3.2 2.5.6 3.6.1.3 0 .7-.2 1z"/></svg>
      <span class="phone-number" style="font-size:16px;">0400 555 218</span>
    </div>
    <div class="contact" style="font-size:8.5px; gap:5px;">
      <svg width="9" height="9" viewBox="0 0 24 24"><circle cx="12" cy="12" r="10" fill="none" stroke="var(--teal)" stroke-width="2"/><path d="M2 12h20M12 2c3 3 3 17 0 20M12 2c-3 3-3 17 0 20" fill="none" stroke="var(--teal)" stroke-width="2"/></svg>
      www.harbourlinelettings.com.au
    </div>
    <div class="contact" style="font-size:8.5px; gap:5px;">
      <svg width="9" height="7" viewBox="0 0 24 18"><path d="M0 0h24v2L12 10 0 2zM0 4l12 8 12-8v14H0z"/></svg>
      referrals@harbourlinelettings.com.au
    </div>
  </div>
  <div class="abs fine" style="left:570px; top:246px; width:530px;">
    <span class="fine__label">Fine Print:</span>
    <p class="fine__text">* $250 referral fee paid when the owner you refer signs their property for Management with Harbourline Lettings Group. Your referral must be submitted prior to a signing on our website using the referral form on this page: <b>http://www.harbourlinelettings.com.au/referral-program/</b></p>
  </div>
</section>

<!-- Banner with slanted photo edge -->
<section class="banner banner--slant">
  <svg class="art" width="1110" height="276" viewBox="0 0 1110 276">
    <defs>
      <linearGradient id="streetB" x1="0" y1="0" x2="0" y2="1">
        <stop offset="0" stop-color="#4a9ad8"/>
        <stop offset=".4" stop-color="#bfc6c8"/>
        <stop offset=".68" stop-color="#4f7a3a"/>
        <stop offset="1" stop-color="#a9a59c"/>
      </linearGradient>
    </defs>
    <polygon role="img" aria-label="Photo of modern terraced homes on a leafy hillside street" points="0,0 620,0 550,276 0,276" fill="url(#streetB)"/>
    <polygon points="620,0 632,0 562,276 550,276" fill="var(--teal)"/>
  </svg>
  <div class="abs brand" style="left:360px; top:38px; font-size:13px;"><span class="brand__mark"></span>HARBOURLINE LETTINGS GROUP</div>
  <div class="abs headline" style="left:642px; top:38px; font-size:26px;">Invite your friends and receive</div>
  <div class="abs offer" style="left:642px; top:78px; font-size:16.5px;"><span class="offer__amount">$250</span>and they get 2 months free management! *</div>
  <div class="abs contact" style="left:642px; top:140px; gap:14px;">
    <svg width="18" height="18" viewBox="0 0 24 24"><path d="M6.6 10.8a15 15 0 0 0 6.6 6.6l2.2-2.2c.3-.3.7-.4 1-.2 1.1.4 2.3.6 3.6.6.6 0 1 .4 1 1V20c0 .6-.4 1-1 1A17 17 0 0 1 3 4c0-.6.4-1 1-1h3.5c.6 0 1 .4 1 1 0 1.3.2 2.5.6 3.6.1.3 0 .7-.2 1z"/></svg>
    <span class="phone-number" style="font-size:28px;">0400 555 218</span>
  </div>
  <div class="abs contact" style="left:644px; top:182px; font-size:13.5px; gap:18px;">
    <svg width="12" height="12" viewBox="0 0 24 24"><circle cx="12" cy="12" r="10" fill="none" stroke="var(--teal)" stroke-width="2"/><path d="M2 12h20M12 2c3 3 3 17 0 20M12 2c-3 3-3 17 0 20" fill="none" stroke="var(--teal)" stroke-width="2"/></svg>
    www.harbourlinelettings.com.au
  </div>
  <div class="abs contact" style="left:644px; top:206px; font-size:13.5px; gap:18px;">
    <svg width="12" height="9" viewBox="0 0 24 18"><path d="M0 0h24v2L12 10 0 2zM0 4l12 8 12-8v14H0z"/></svg>
    referrals@harbourlinelettings.com.au
  </div>
  <div class="abs fine" style="left:566px; top:246px; width:530px;">
    <span class="fine__label">Fine Print:</span>
    <p class="fine__text">* $250 referral fee paid when the owner you refer signs their property for Management with Harbourline Lettings Group. Your referral must be submitted prior to a signing on our website using the referral form on this page: <b>http://www.harbourlinelettings.com.au/referral-program/</b></p>
  </div>
</section>

<!-- Banner with diamond mosaic -->
<section class="banner banner--mosaic">
  <svg class="art" width="1108" height="274" viewBox="0 0 1108 274">
    <defs>
      <linearGradient id="tileHouse" x1="0" y1="0" x2="0" y2="1"><stop offset="0" stop-color="#5fa9d8"/><stop offset=".6" stop-color="#dcdcd8"/><stop offset="1" stop-color="#7a8a6a"/></linearGradient>
      <linearGradient id="tileSea" x1="0" y1="0" x2="0" y2="1"><stop offset="0" stop-color="#3c7fb8"/><stop offset="1" stop-color="#1d4e7a"/></linearGradient>
      <linearGradient id="tileRoom" x1="0" y1="0" x2="0" y2="1"><stop offset="0" stop-color="#eef0ee"/><stop offset="1" stop-color="#c9cfcc"/></linearGradient>
      <linearGradient id="tileLounge" x1="0" y1="0" x2="1" y2="1"><stop offset="0" stop-color="#e8e6e0"/><stop offset="1" stop-color="#9fb6c4"/></linearGradient>
    </defs>
    <g role="img" aria-label="Mosaic of diamond-shaped photos: modern homes, ocean view, kitchen and living room">
      <polygon points="1000,-46 1080,34 1000,114 920,34" fill="url(#tileHouse)"/>
      <polygon points="896,32 976,112 896,192 816,112" fill="url(#tileHouse)"/>
      <polygon points="1086,44 1166,124 1086,204 1006,124" fill="url(#tileSea)"/>
      <polygon points="830,128 910,208 830,288 750,208" fill="url(#tileRoom)"/>
      <polygon points="1000,128 1080,208 1000,288 920,208" fill="url(#tileLounge)"/>
    </g>
    <polygon points="830,274 750,194 750,274" fill="var(--teal)"/>
    <polygon points="1108,206 1108,274 1040,274" fill="var(--teal)"/>
    <polygon points="920,274 960,234 1000,274" fill="var(--teal-light)"/>
    <polygon points="960,0 1000,0 980,20" fill="var(--teal-light)"/>
  </svg>
  <div class="abs brand" style="left:262px; top:44px; font-size:16px;"><span class="brand__mark"></span>HARBOURLINE LETTINGS GROUP</div>
  <div class="abs offer" style="left:30px; top:110px; font-size:17.5px;">Invite your friends and receive <span class="offer__amount">$250</span> and they get 2 months free management! *</div>
  <div class="abs contact" style="left:36px; top:162px; gap:24px;">
    <svg width="34" height="28" viewBox="0 0 36 30"><path d="M3 8c0-4 6-6 15-6s15 2 15 6v3h-7V8c-2-1-5-1-8-1s-6 0-8 1v3H3z"/><path d="M8 13h20l4 15H4z"/><circle cx="18" cy="20" r="4" fill="#fff"/></svg>
    <span class="phone-number" style="font-size:31px;">0400 555 218</span>
  </div>
  <div class="divider" style="left:350px; top:156px; width:2px; height:46px;"></div>
  <div class="abs contact" style="left:376px; top:160px; font-size:16px; gap:18px;">
    <svg width="14" height="14" viewBox="0 0 24 24"><circle cx="12" cy="12" r="10" fill="none" stroke="var(--teal)" stroke-width="2"/><path d="M2 12h20M12 2c3 3 3 17 0 20M12 2c-3 3-3 17 0 20" fill="none" stroke="var(--teal)" stroke-width="2"/></svg>
    www.harbourlinelettings.com.au
  </div>
  <div class="abs contact" style="left:376px; top:186px; font-size:16px; gap:18px;">
    <svg width="14" height="10" viewBox="0 0 24 18"><path d="M0 0h24v2L12 10 0 2zM0 4l12 8 12-8v14H0z"/></svg>
    referrals@harbourlinelettings.com.au
  </div>
  <div class="abs fine" style="left:24px; top:230px; width:720px;">
    <span class="fine__label">Fine Print:</span>
    <p class="fine__text">* $250 referral fee paid when the owner you refer signs their property for Management with Harbourline Lettings Group. Your referral must be submitted prior to signing on our website using the referral form on this page: http://www.harbourlinelettings.com.au/referral-program/</p>
  </div>
</section>

</body>
</html>
```